Need a graphic design for front page of tech blog

Hi,

So I'm looking to start a project of redesigning the front homepage for all of my tech sites. I already have a developer that will code the change, so what I need from someone here is to give me a graphic design, which I can then give to my developers to code.

Currently, I have the plain old boring default list of WordPress posts as the front page, which needs to be replaced with something a little more like a magazine or newspaper style. You can see my four sites here:

https://www.quill-gadget-notes.com/
https://servicebenchnerd.com/
https://theatticbitworks.com/
https://www.hoppingtolark.com/

I've attached some screenshots of mobile sites that I like in terms of look and style. Some desktop sites that I like are here (I like some parts more than others, I've attached screenshots of the sections I like):

https://www.ploddernook.com/
https://www.gizmonest.com/
https://www.pinewirebulletin.com/
https://www.takeholdwith.com/
https://www.dayspool.com/

Basically, I don't need all that text after each post. Seems like most sites now just have an image, a title, the author and date info and possibly the category.

Right now I'm only showing 10 posts and one has to scroll through lots of text to see them all. The sidebar is good, but I think we can get rid of that for the front page and instead have different sections like Latest Tips, and then some section headers based on the categories.

Anyway, I'm looking for someone who can come up with multiple designs, so that I have some choice.

I'm looking to get this done over the next few weeks. Also, please include in your price the cost of any revisions and how many revisions can be done.

Thanks

Tarun

```html
<!DOCTYPE html>
<html lang="en">
<head>
<meta charset="utf-8">
<title>Tech Blog Front Page</title>
<link rel="stylesheet" href="https://fonts.googleapis.com/css2?family=Roboto:wght@400;500;700&display=swap">
<style>
:root{
  --navy:#0e1a45;
  --navy-deep:#0a1233;
  --accent:#2f8ff0;
  --accent-band:#2f9af3;
  --white:#ffffff;
  --meta:#2c3c6c;
  --ink:#0e1a45;
}
*{box-sizing:border-box;margin:0;padding:0}
html,body{width:1200px;height:2222px;overflow:hidden}
body{position:relative;background:var(--navy);font-family:'Roboto',sans-serif;color:var(--white)}
.abs{position:absolute}

/* header */
.logo-box{left:75px;top:12px;width:241px;height:40px;background:var(--navy-deep)}
.search{left:465px;top:14px;width:267px;height:28px;border-bottom:1px solid var(--accent)}
.search svg{position:absolute;right:4px;top:2px}
.menu{left:1098px;top:22px}

/* section headings */
.section-head{left:0;width:1200px;height:60px}
.section-title{position:absolute;font-weight:700;font-size:44px;line-height:1;color:var(--white)}
.section-title::before{content:"";position:absolute;left:-73px;bottom:2px;width:60px;height:1px;background:var(--accent)}
.see-more{position:absolute;left:1035px;font-size:10px;color:var(--accent);display:flex;align-items:center;gap:13px}

/* card rows */
.card-row{left:75px;display:grid;grid-template-columns:repeat(4,246px);column-gap:21px}
.card{position:relative;display:flex;flex-direction:column;align-items:center}
.card-image{width:246px}
.card-meta{width:100%;display:flex;justify-content:space-between;align-items:center;margin-top:14px;font-size:9px;color:var(--meta)}
.card-author{display:flex;align-items:center;gap:5px}
.avatar{width:14px;height:14px;border-radius:50%;background:#c9ccd6}
.card-title{margin-top:15px;width:210px;text-align:center;font-size:13px;line-height:18px;font-weight:400;color:var(--white)}
.tag{margin-top:27px;width:138px;height:24px;border:1px solid var(--accent);border-radius:12px;display:flex;align-items:center;justify-content:center;font-size:10px;color:var(--accent)}
.highlight-frame{left:335px;top:321px;width:261px;height:245px;border:1px solid var(--accent)}

.img-film{background:linear-gradient(135deg,#2d4f9a 0%,#1c3470 40%,#7a4a3a 60%,#1a2a60 100%)}
.img-chat{background:linear-gradient(160deg,#a9dce9 0%,#86c6dd 60%,#e88a6a 100%)}
.img-desk{background:linear-gradient(180deg,#5a6480 0%,#6d6a72 55%,#5b4a45 100%)}
.img-keys{background:linear-gradient(150deg,#6e7fa8 0%,#3c4f86 55%,#1d2c5e 100%)}
.img-phone{background:linear-gradient(135deg,#c8cfdf 0%,#5d6888 55%,#27335e 100%)}
.img-laptop{background:linear-gradient(160deg,#5b6584 0%,#2b3558 60%,#1a2347 100%)}
.img-eye{background:linear-gradient(135deg,#3b4462 0%,#4a4a5a 45%,#2a3f7a 65%,#262f52 100%)}

/* subscribe band */
.subscribe-band{left:0;top:1698px;width:1200px;height:232px;background:var(--accent-band)}
.subscribe-band .section-title::before{background:var(--white)}
.email-field{left:387px;top:1848px;width:375px;height:22px;border-bottom:1px solid var(--white);font-size:12px;color:var(--white)}
.subscribe-action{left:800px;top:1844px;display:flex;align-items:center;gap:12px;font-size:16px;color:var(--ink)}

/* footer */
.footer-col{top:1988px;width:300px;text-align:center}
.footer-head{font-size:16px;font-weight:400;color:var(--accent);margin-bottom:34px}
.footer-links{list-style:none;font-size:12px;line-height:28px;color:var(--accent)}
.footer-divider{top:1979px;width:1px;height:196px;background:var(--accent)}
.social{display:flex;justify-content:center;gap:30px;font-size:13px;color:var(--accent);margin-top:8px}
.social span{display:flex;align-items:center;gap:6px}
.social i{display:block;width:8px;height:8px;border-radius:50%;background:var(--accent)}
</style>
</head>
<body>

<header>
  <div class="abs logo-box" aria-label="Site logo area"></div>
  <div class="abs search">
    <svg width="18" height="18" viewBox="0 0 18 18" fill="none" stroke="#2f8ff0" stroke-width="1.3"><circle cx="11" cy="7" r="5"/><line x1="7.5" y1="10.5" x2="2" y2="16"/></svg>
  </div>
  <svg class="abs menu" width="26" height="16" viewBox="0 0 26 16" stroke="#2f8ff0" stroke-width="1.5"><line x1="4" y1="2" x2="26" y2="2"/><line x1="0" y1="14" x2="26" y2="14"/></svg>
</header>

<!-- Featured -->
<div class="abs section-head" style="top:120px">
  <h2 class="section-title" style="left:511px;top:2px">Featured</h2>
  <a class="see-more" style="top:20px">See more <svg width="30" height="14" viewBox="0 0 30 14" fill="none" stroke="#2f8ff0" stroke-width="1.3"><line x1="0" y1="7" x2="29" y2="7"/><polyline points="22,1 29,7 22,13"/></svg></a>
</div>
<div class="abs highlight-frame"></div>
<section class="abs card-row" style="top:230px">
  <article class="card"><div class="card-image img-film" style="height:188px" role="img" aria-label="Film strip photo"></div><div class="card-meta"><span>27.02.2019</span><span class="card-author">by Lena Marsh <i class="avatar"></i></span></div><h3 class="card-title">Best Free Team Chat Software for Panelix 10</h3><span class="tag">Tools Review</span></article>
  <article class="card"><div class="card-image img-chat" style="height:188px" role="img" aria-label="Illustration of a phone with chat messages"></div><div class="card-meta"><span>27.02.2019</span><span class="card-author">by Lena Marsh <i class="avatar"></i></span></div><h3 class="card-title">Best Free Team Chat Software for Panelix 10</h3><span class="tag">Tools Review</span></article>
  <article class="card"><div class="card-image img-desk" style="height:188px" role="img" aria-label="Desk with computer and keyboard photo"></div><div class="card-meta"><span>27.02.2019</span><span class="card-author">by Lena Marsh <i class="avatar"></i></span></div><h3 class="card-title">Best Free Team Chat Software for Panelix 10</h3><span class="tag">Tools Review</span></article>
  <article class="card"><div class="card-image img-keys" style="height:188px" role="img" aria-label="Keyboard close-up photo"></div><div class="card-meta"><span>27.02.2019</span><span class="card-author">by Lena Marsh <i class="avatar"></i></span></div><h3 class="card-title">Best Free Team Chat Software for Panelix 10</h3><span class="tag">Tools Review</span></article>
</section>

<!-- Recent -->
<div class="abs section-head" style="top:656px">
  <h2 class="section-title" style="left:530px;top:4px">Recent</h2>
  <a class="see-more" style="top:24px">See more <svg width="30" height="14" viewBox="0 0 30 14" fill="none" stroke="#2f8ff0" stroke-width="1.3"><line x1="0" y1="7" x2="29" y2="7"/><polyline points="22,1 29,7 22,13"/></svg></a>
</div>
<section class="abs card-row" style="top:784px">
  <article class="card"><div class="card-image img-phone" style="height:136px" role="img" aria-label="Hand holding a phone photo"></div><div class="card-meta"><span>27.02.2019</span><span class="card-author">by Lena Marsh <i class="avatar"></i></span></div><h3 class="card-title">Best Free Team Chat Software for Panelix 10</h3><span class="tag">Tools Review</span></article>
  <article class="card"><div class="card-image img-laptop" style="height:136px" role="img" aria-label="Laptop on a desk photo"></div><div class="card-meta"><span>27.02.2019</span><span class="card-author">by Lena Marsh <i class="avatar"></i></span></div><h3 class="card-title">Best Free Team Chat Software for Panelix 10</h3><span class="tag">Tools Review</span></article>
  <article class="card"><div class="card-image img-eye" style="height:136px" role="img" aria-label="Close-up eye photo"></div><div class="card-meta"><span>27.02.2019</span><span class="card-author">by Lena Marsh <i class="avatar"></i></span></div><h3 class="card-title">Best Free Team Chat Software for Panelix 10</h3><span class="tag">Tools Review</span></article>
  <article class="card"><div class="card-image img-chat" style="height:136px" role="img" aria-label="Illustration of a phone with chat messages"></div><div class="card-meta"><span>27.02.2019</span><span class="card-author">by Lena Marsh <i class="avatar"></i></span></div><h3 class="card-title">Best Free Team Chat Software for Panelix 10</h3><span class="tag">Tools Review</span></article>
</section>

<!-- Trending -->
<div class="abs section-head" style="top:1146px">
  <h2 class="section-title" style="left:511px;top:2px">Trending</h2>
  <a class="see-more" style="top:22px">See more <svg width="30" height="14" viewBox="0 0 30 14" fill="none" stroke="#2f8ff0" stroke-width="1.3"><line x1="0" y1="7" x2="29" y2="7"/><polyline points="22,1 29,7 22,13"/></svg></a>
</div>
<section class="abs card-row" style="top:1270px">
  <article class="card"><div class="card-image img-film" style="height:186px" role="img" aria-label="Film strip photo"></div><div class="card-meta"><span>27.02.2019</span><span class="card-author">by Lena Marsh <i class="avatar"></i></span></div><h3 class="card-title">Best Free Team Chat Software for Panelix 10</h3><span class="tag">Tools Review</span></article>
  <article class="card"><div class="card-image img-chat" style="height:186px" role="img" aria-label="Illustration of a phone with chat messages"></div><div class="card-meta"><span>27.02.2019</span><span class="card-author">by Lena Marsh <i class="avatar"></i></span></div><h3 class="card-title">Best Free Team Chat Software for Panelix 10</h3><span class="tag">Tools Review</span></article>
  <article class="card"><div class="card-image img-desk" style="height:186px" role="img" aria-label="Desk with computer and keyboard photo"></div><div class="card-meta"><span>27.02.2019</span><span class="card-author">by Lena Marsh <i class="avatar"></i></span></div><h3 class="card-title">Best Free Team Chat Software for Panelix 10</h3><span class="tag">Tools Review</span></article>
  <article class="card"><div class="card-image img-keys" style="height:186px" role="img" aria-label="Keyboard close-up photo"></div><div class="card-meta"><span>27.02.2019</span><span class="card-author">by Lena Marsh <i class="avatar"></i></span></div><h3 class="card-title">Best Free Team Chat Software for Panelix 10</h3><span class="tag">Tools Review</span></article>
</section>

<!-- Subscribe -->
<section class="abs subscribe-band">
  <h2 class="section-title" style="left:499px;top:44px">Subscribe</h2>
</section>
<div class="abs email-field">Email Address</div>
<div class="abs subscribe-action">Subscribe <svg width="30" height="14" viewBox="0 0 30 14" fill="none" stroke="#0e1a45" stroke-width="1.3"><line x1="0" y1="7" x2="29" y2="7"/><polyline points="22,1 29,7 22,13"/></svg></div>

<!-- Footer -->
<footer>
  <div class="abs footer-col" style="left:40px">
    <h4 class="footer-head">Main Sections</h4>
    <ul class="footer-links"><li>Featured</li><li>Recent</li><li>Trending</li><li>Suscribe</li></ul>
  </div>
  <div class="abs footer-divider" style="left:385px"></div>
  <div class="abs footer-col" style="left:448px">
    <h4 class="footer-head">Other</h4>
    <ul class="footer-links"><li>About</li><li>Contact</li><li>Privacy Policy</li></ul>
  </div>
  <div class="abs footer-divider" style="left:813px"></div>
  <div class="abs footer-col" style="left:863px">
    <h4 class="footer-head">Find us here:</h4>
    <div class="social"><span><i></i>Lenswall</span><span>Shortpost</span><span>Friendhub</span></div>
  </div>
</footer>

</body>
</html>
```